Flyer-Design für online Buchverkaufsseite
Zielgruppe
Wir sind eine Onlien Ankaufsseite für Bücher.Wir kaufen Bücher zum Festpreis. Unsere Zielgruppe sind alle Haushalte, die ihre gebrauchten Bücher verkaufen wollen.
Aufgabenstellung
Nicht so viel Text reinpacken, alle wichtige Punkte sollen großer Schriftformat dargestellt werden.
Text soll vom Designer selbst erstellt werden.

```html
<!DOCTYPE html>
<html lang="de">
<head>
<meta charset="utf-8">
<title>Flyer – Zu viele Bücher? Jetzt verkaufen!</title>
<link rel="stylesheet" href="https://fonts.googleapis.com/css2?family=Jost:wght@600;700&display=swap">
<style>
  :root {
    --stage: #a6eef8;
    --paper: #ffffff;
    --teal-light: #2f8f8c;
    --teal: #1b7488;
    --teal-deep: #136a86;
    --photo-top: #d9dde2;
    --photo-mid: #a9b6c8;
    --photo-low: #eef0f2;
  }
  * { margin: 0; padding: 0; box-sizing: border-box; }
  html, body {
    width: 1200px; height: 1200px; overflow: hidden;
    background: var(--stage);
  }
  .flyer {
    position: absolute;
    left: 230px; top: 45px;
    width: 740px; height: 1110px;
    background: var(--paper);
    overflow: hidden;
    font-family: "Jost", "Futura", sans-serif;
    font-weight: 700;
  }
  .flyer__photo {
    position: absolute; inset: 0 0 180px 0;
    background:
      radial-gradient(ellipse 55% 35% at 78% 30%, var(--photo-mid) 0%, rgba(169,182,200,0) 70%),
      linear-gradient(180deg, var(--photo-top) 0%, #e4e7ea 50%, var(--photo-low) 80%, var(--paper) 100%);
  }
  .headline {
    position: absolute; left: 0;
    line-height: 1;
    white-space: nowrap;
    text-transform: uppercase;
  }
  .headline--question-a {
    top: 412px; left: 186px;
    font-size: 138px; letter-spacing: -1px;
    color: var(--teal-light);
  }
  .headline--question-b {
    top: 522px; left: -4px;
    font-size: 146px; letter-spacing: -2px;
    color: var(--teal);
  }
  .headline--action-a {
    top: 665px; left: -18px;
    font-size: 176px; letter-spacing: -4px;
    color: var(--teal-deep);
    transform: scaleX(0.86); transform-origin: left center;
  }
  .headline--action-b {
    top: 818px; left: 16px;
    font-size: 112px; letter-spacing: 1px;
    color: var(--teal-deep);
  }
  .brand {
    position: absolute; left: 90px; top: 980px;
    display: flex; align-items: center; gap: 16px;
  }
  .brand__dot {
    width: 86px; height: 86px; border-radius: 50%;
    background: var(--teal);
  }
  .brand__name {
    font-weight: 600; font-size: 78px; line-height: 1;
    color: var(--teal);
  }
</style>
</head>
<body>
  <main class="flyer">
    <div class="flyer__photo" role="img" aria-label="Foto: Person in Jeans sitzt lesend auf einem Stapel Bücher, heller Hintergrund"></div>
    <h1>
      <span class="headline headline--question-a">Zu viele</span>
      <span class="headline headline--question-b">Bücher?</span>
      <span class="headline headline--action-a">Jetzt</span>
      <span class="headline headline--action-b">Verkaufen!</span>
    </h1>
    <div class="brand">
      <span class="brand__dot"></span>
      <span class="brand__name">buchflink.de</span>
    </div>
  </main>
</body>
</html>
```